Online Course Page

We are building a video based online course page. This project is for only the actual page that the student will watch the videos at. They will watch one vide at a time. Once one video lesson is completed then they can move to the next video lesson. The page will need to show the video player. (Main feature.) The list of lessons in the course. Instructor information. Profile picture and bio of the instructor. A Live chat button that will initiate a chat in real-time with the instructor.

The winning designer will also be asked to to design the dashboard area and other aspects of the user interface as an additional project.

Target Market(s)

Adults

Number of Pages Required

1 page

Colors
9bcb3c

Requirements
Must have
• Our logo is attached. Green and grey are our colors. Should feel modern, clean and be simple to navigate. The site will be responsive so the layout should work well on mobile devices.

```html
<!DOCTYPE html>
<html lang="en">
<head>
<meta charset="utf-8">
<title>LearnHarbor – Course Player</title>
<link href="https://fonts.googleapis.com/css2?family=Open+Sans:wght@400;600;700&display=swap" rel="stylesheet">
<style>
:root{
  --green:#8dc63f;
  --green-dark:#6fa52c;
  --green-soft:#dfead0;
  --green-line:#cddcb8;
  --grey-panel:#f1f1f1;
  --grey-head:#f6f6f6;
  --grey-row:#e2e2e2;
  --grey-text:#555;
  --ink:#1e1e1e;
  --rule:#d6d6d6;
  --video:#94c3d5;
  --link:#1aafe0;
  --footer:#3b3b3b;
  --white:#fff;
}
*{box-sizing:border-box;margin:0;padding:0}
html,body{width:1200px;height:1200px;overflow:hidden}
body{
  font-family:'Open Sans',sans-serif;
  background:radial-gradient(ellipse at 50% 50%,#8fc843 0%,#7ab532 60%,#69a028 100%);
  position:relative;
}
.page{position:absolute;left:114px;top:0;width:984px;height:1200px;background:var(--white)}
.sidebar{position:absolute;left:0;top:0;width:236px;height:1163px;background:var(--grey-panel)}
.sidebar-head{height:46px;background:var(--grey-head);position:relative;border-bottom:1px solid #e4e4e4}
.back{position:absolute;left:12px;top:13px}
.brand{position:absolute;left:80px;top:13px;display:flex;align-items:center;gap:6px;font-size:13px;font-weight:700;color:#4a4a4a}
.brand-dot{width:12px;height:12px;border-radius:50%;background:var(--green)}
.course-title{height:44px;line-height:44px;text-align:center;font-size:13px;color:var(--grey-text);letter-spacing:.3px}
.search{position:absolute;left:12px;top:102px;width:212px;height:21px;border:1px solid var(--green);background:var(--white);font-size:10px;color:#b3b3b3;line-height:19px;padding-left:10px}
.search svg{position:absolute;right:6px;top:4px}
.lessons{position:absolute;left:0;top:136px;width:236px;list-style:none}
.lesson{height:39px;display:flex;align-items:center;padding:0 9px 0 11px;background:var(--green-soft);border-bottom:1px solid var(--green-line);font-size:12px;color:#333}
.lesson .name{flex:1;margin-left:12px}
.lesson .time{font-size:10.5px;color:#777}
.lesson.intro{height:36px;background:var(--grey-row);border-bottom:none;color:#444}
.lesson.active{background:var(--green);color:var(--white);font-weight:600}
.lesson.active .time{color:var(--white);font-weight:400}
.topbar{position:absolute;left:236px;top:0;width:748px;height:46px;background:var(--green);color:var(--white);text-align:center;font-size:17px;font-weight:600;line-height:46px}
.topbar svg{position:absolute;left:12px;top:13px}
.video{position:absolute;left:244px;top:54px;width:732px;height:441px;background:linear-gradient(135deg,#9ac8da,#8fbfd1)}
.play{position:absolute;left:410px;top:170px}
.chat-btn{position:absolute;left:888px;top:454px;width:96px;height:30px;background:var(--green);color:var(--white);font-size:11.5px;display:flex;align-items:center;gap:6px;padding-left:11px}
.section-title{position:absolute;font-size:23px;color:var(--green);font-weight:400;line-height:1}
.rule{position:absolute;height:1px;background:var(--rule)}
.rule-accent{position:absolute;height:2px;background:var(--green)}
.lesson-text{position:absolute;left:258px;top:574px;width:720px;font-size:14.3px;line-height:22px;color:var(--ink);text-indent:130px}
.photo-back{position:absolute;background:#c8e3a3}
.photo{position:absolute;left:259px;top:757px;width:146px;height:194px;background:linear-gradient(160deg,#1d3a33,#0d1a17 60%,#2c5248);border:1px solid var(--green)}
.inst-name{position:absolute;left:436px;top:757px;font-size:14px;color:var(--link)}
.inst-role{position:absolute;left:436px;top:788px;font-size:15px;font-weight:700;color:var(--ink)}
.inst-bio{position:absolute;left:437px;top:812px;width:520px;font-size:11.8px;line-height:19.2px;color:#2a2a2a}
.inst-bio p+p{margin-top:19px}
.footer{position:absolute;left:0;top:1163px;width:984px;height:37px;background:var(--footer);color:#ddd;font-size:11px;line-height:37px}
.footer span{position:absolute}
</style>
</head>
<body>
<div class="page">
  <aside class="sidebar">
    <div class="sidebar-head">
      <svg class="back" width="12" height="20" viewBox="0 0 12 20"><path d="M10 1 1 10l9 9" fill="none" stroke="#888" stroke-width="1.5"/></svg>
      <div class="brand"><span class="brand-dot"></span>LearnHarbor</div>
    </div>
    <div class="course-title">COURSE TITLE</div>
    <div class="search">Search Course Content
      <svg width="12" height="12" viewBox="0 0 12 12"><circle cx="5" cy="5" r="3.8" fill="none" stroke="#8dc63f" stroke-width="1.4"/><path d="M8 8l3 3" stroke="#8dc63f" stroke-width="1.6"/></svg>
    </div>
    <ul class="lessons">
      <li class="lesson intro"><svg width="16" height="16" viewBox="0 0 16 16"><circle cx="8" cy="8" r="7" fill="none" stroke="#999"/><path d="M6.3 5v6l5-3z" fill="#999"/></svg><span class="name">Intro of Lorem Ip</span><span class="time">02:30</span></li>
      <li class="lesson active"><svg width="16" height="16" viewBox="0 0 16 16"><circle cx="8" cy="8" r="8" fill="#fff"/><rect x="5.5" y="5" width="1.8" height="6" fill="#8dc63f"/><rect x="8.7" y="5" width="1.8" height="6" fill="#8dc63f"/></svg><span class="name">Part 1</span><span class="time">02:30</span></li>
      <li class="lesson"><svg width="16" height="16" viewBox="0 0 16 16"><circle cx="8" cy="8" r="8" fill="#8dc63f"/><path d="M6.3 4.8v6.4l5-3.2z" fill="#fff"/></svg><span class="name">Part 2</span><span class="time">02:30</span></li>
      <li class="lesson"><svg width="16" height="16" viewBox="0 0 16 16"><circle cx="8" cy="8" r="8" fill="#8dc63f"/><path d="M6.3 4.8v6.4l5-3.2z" fill="#fff"/></svg><span class="name">Part 3</span><span class="time">02:30</span></li>
      <li class="lesson"><svg width="16" height="16" viewBox="0 0 16 16"><circle cx="8" cy="8" r="8" fill="#8dc63f"/><path d="M6.3 4.8v6.4l5-3.2z" fill="#fff"/></svg><span class="name">Part 4</span><span class="time">02:30</span></li>
      <li class="lesson"><svg width="16" height="16" viewBox="0 0 16 16"><circle cx="8" cy="8" r="8" fill="#8dc63f"/><path d="M6.3 4.8v6.4l5-3.2z" fill="#fff"/></svg><span class="name">Part 5</span><span class="time">02:30</span></li>
      <li class="lesson"><svg width="16" height="16" viewBox="0 0 16 16"><circle cx="8" cy="8" r="8" fill="#8dc63f"/><path d="M6.3 4.8v6.4l5-3.2z" fill="#fff"/></svg><span class="name">Part 6</span><span class="time">02:30</span></li>
      <li class="lesson"><svg width="16" height="16" viewBox="0 0 16 16"><circle cx="8" cy="8" r="8" fill="#8dc63f"/><path d="M6.3 4.8v6.4l5-3.2z" fill="#fff"/></svg><span class="name">Part 7</span><span class="time">02:30</span></li>
      <li class="lesson"><svg width="16" height="16" viewBox="0 0 16 16"><circle cx="8" cy="8" r="8" fill="#8dc63f"/><path d="M6.3 4.8v6.4l5-3.2z" fill="#fff"/></svg><span class="name">Part 8</span><span class="time">02:30</span></li>
      <li class="lesson"><svg width="16" height="16" viewBox="0 0 16 16"><circle cx="8" cy="8" r="8" fill="#8dc63f"/><path d="M6.3 4.8v6.4l5-3.2z" fill="#fff"/></svg><span class="name">Part 9</span><span class="time">02:30</span></li>
      <li class="lesson"><svg width="16" height="16" viewBox="0 0 16 16"><circle cx="8" cy="8" r="8" fill="#8dc63f"/><path d="M6.3 4.8v6.4l5-3.2z" fill="#fff"/></svg><span class="name">End</span><span class="time">02:30</span></li>
    </ul>
  </aside>

  <header class="topbar">
    <svg width="20" height="20" viewBox="0 0 20 20"><circle cx="10" cy="10" r="9" fill="none" stroke="#fff" stroke-width="1.3"/><path d="M6 7h8M6 10h8M6 13h8" stroke="#fff" stroke-width="1.3"/></svg>
    Intro of Lorem Ip
  </header>

  <div class="video" role="img" aria-label="Video thumbnail: webinar illustration with a laptop and presenter on a light blue background">
    <svg class="play" width="74" height="74" viewBox="0 0 74 74"><circle cx="37" cy="37" r="37" fill="#fff" opacity=".9"/><path d="M29 23v28l23-14z" fill="#94c3d5"/></svg>
  </div>
  <div class="chat-btn">
    <svg width="20" height="16" viewBox="0 0 20 16"><path d="M2 2h11v8H6l-3 3v-3H2z" fill="none" stroke="#fff" stroke-width="1.4"/><path d="M15 5h3v7h-1v2l-2-2h-5" fill="none" stroke="#fff" stroke-width="1.4"/></svg>
    Live chat
  </div>

  <h2 class="section-title" style="left:256px;top:521px">Lesion info</h2>
  <div class="rule" style="left:254px;top:548px;width:722px"></div>
  <div class="rule-accent" style="left:254px;top:547px;width:119px"></div>
  <p class="lesson-text">Lorem ipsum dolor sit amet, consectetuer adipiscing elit. Aenean commodo ligula eget dolor. Aenean massa. Cum sociis natoque pec natibus et magnis dis parturient montes, nascetur ridiculus mus.&nbsp; Donec quam felis, ultricies nec, pellentvesque feveu, pretium quis, sem. Nulla consequat massa quis enim. Donec pede justo, fringilla vel, aliquet nec, vulputate eget, arcu.</p>

  <h2 class="section-title" style="left:255px;top:706px">About the Instructors</h2>
  <div class="rule" style="left:240px;top:732px;width:740px"></div>
  <div class="rule-accent" style="left:254px;top:730px;width:228px"></div>

  <div class="photo-back" style="left:250px;top:755px;width:152px;height:200px;transform:rotate(-3deg)"></div>
  <div class="photo-back" style="left:262px;top:753px;width:150px;height:200px;transform:rotate(2deg);background:#b7da86"></div>
  <div class="photo" role="img" aria-label="Instructor portrait photo"></div>

  <div class="inst-name">Marco Ellison</div>
  <div class="inst-role">Interaction Designer</div>
  <div class="inst-bio">
    <p>Lorem ipsum dolor sit amet, consectetuer adipiscing elicddenean commodo ligula eget dolor. Aenean massa. Cum socibfgbis natbe pec natibus et magnis dis parturient montes, nascetur ridiculus mus.&nbsp; Donecdv quagfbm felis, ultricies nec, pellentvesque feveu, pretium quis, sem. Nusequat massa quis enbfim.</p>
    <p>Donec pede justo, fringilla vel, aliquet nec, vulputate eget, arcu. enim. Donec pede justo, frin-bfbgilla vel, aliquet nec, vulputate. in enim justo, rhoncus ut, imperdiet a, venenatis vitae, jubf-bfsto. Nullam dictum felis eu pede mollis pretium. Integer tincidunt. Cras dapibus. Vivamus eleentum semper nisi. Aenean vulputate eleifend tellus. Aenean leo ligula, porttitor eu, con-sequat vitabe, eleifend ac, enim. Aliquam lorem ante, dapibus in, viverra quis, feugiat a, tellus. Phasellus viverra nulla ut metus varius laoreet. Quisque rutrum. Aenean imperdiet. Etiam ult nisi vel augue. Curabitur ullamcorper ultricies nisi. Nam eget dui. Etiam rhoncus. Maecenas tempus, tellus</p>
  </div>

  <footer class="footer">
    <span style="left:29px">Copyright &nbsp;© LearnHarbor, 2018</span>
    <span style="left:588px">Terms</span>
    <span style="left:650px">|</span>
    <span style="left:684px">Privacy Policy and Cookie Policy</span>
    <span style="left:868px">|</span>
    <span style="left:902px">Contect Us</span>
  </footer>
</div>
</body>
</html>
```